Banner Ads for CopperLeafLoans

Required elements: (in order of importance)
-
Headline: ALERT – Unexpected Drop in Mortgage Rates

Text : Refinance Now at 3.21%APR*

Button text: Calculate New Payment

Logo: CopperLeafLoans (this is required, but should be of low prominence)

Fine print: *Terms & Conditions Apply
-
Look/feel: Completely open (it does NOT need to have any visual reference to CopperLeafLoans site or logo, in fact, I’d prefer it didn’t)

Tone: Credible, straightforward

Specs: 300x250, max file size 30k, swf, gif, or jpg

Suggestions:
- We have found that large prominent rates work well

-Multiple clickable elements usually better than just one

-The brand does not help conversion so should not be very prominent

-Eye catching animation helps (but must stop after 3rd loop and final frame must contain relevant info to stand alone)
Updates

The rate is very important so the 3.21% needs to be large

Logo should be small

You may want to consider exploring a warning sign type visual to go along with the alert messaging

Target Market(s)

Homeowners

Male 40+

Industry/Entity Type

Mortgage

Requirements
Must have
• Required elements: (in order of importance)
-

-
Nice to have
• Suggestions:

```html
<!DOCTYPE html>
<html lang="en">
<head>
<meta charset="utf-8">
<title>CopperLeafLoans Banner Ads</title>
<link rel="stylesheet" href="https://fonts.googleapis.com/css2?family=Anton&family=Arimo:wght@400;700&family=Tinos&display=swap">
<style>
  :root {
    --page: #ffffff;
    --frame: #000000;
    --red: #8f1515;
    --red-light: #a52a2a;
    --band: #d99090;
    --white: #ffffff;
    --ink-dark: #13204a;
    --ink-red: #9a1616;
    --brand: #1e3a78;
    --btn-light: #7fe0ff;
    --btn-dark: #1a8fd0;
    --sign: #f7c600;
  }
  html, body {
    margin: 0;
    width: 1200px;
    height: 900px;
    overflow: hidden;
    background: var(--page);
  }
  .banner {
    position: absolute;
    top: 282px;
    width: 398px;
    height: 330px;
    border: 2px solid var(--frame);
    box-sizing: border-box;
    overflow: hidden;
    background: var(--white);
  }
  .banner--alert { left: 184px; }
  .banner--rate { left: 633px; }
  .hero {
    position: absolute;
    inset: 0 0 72px 0;
    background: linear-gradient(100deg, var(--red-light) 0%, var(--red) 35%, var(--red) 100%);
  }
  .hero-backdrop {
    position: absolute;
    left: 0; top: 0;
    width: 60%; height: 100%;
    background: linear-gradient(160deg, rgba(255,255,255,0.08), rgba(255,255,255,0) 70%);
  }
  .band {
    position: absolute;
    left: 0; right: 0;
    bottom: 64px;
    height: 8px;
    background: linear-gradient(var(--band), #f0d0d0);
  }
  .warning-sign {
    position: absolute;
    left: 140px; top: 14px;
    width: 116px; height: 102px;
  }
  .headline {
    position: absolute;
    left: 0; right: 0; top: 126px;
    margin: 0;
    text-align: center;
    font-family: "Anton", sans-serif;
    font-weight: 400;
    font-size: 30px;
    line-height: 37px;
    color: var(--white);
    letter-spacing: 0.3px;
  }
  .rate-lead {
    position: absolute;
    left: 70px; top: 62px;
    margin: 0;
    font-family: "Anton", sans-serif;
    font-size: 33px;
    line-height: 1;
    color: var(--white);
  }
  .rate-value {
    position: absolute;
    left: 70px; top: 96px;
    margin: 0;
    font-family: "Anton", sans-serif;
    font-size: 86px;
    line-height: 1;
    color: var(--white);
    letter-spacing: -1px;
  }
  .rate-apr {
    position: absolute;
    left: 278px; top: 104px;
    font-family: "Anton", sans-serif;
    font-size: 17px;
    color: var(--white);
  }
  .fine-print {
    position: absolute;
    right: 18px; top: 228px;
    margin: 0;
    font-family: "Arimo", sans-serif;
    font-size: 10.5px;
    color: var(--white);
  }
  .cta-button {
    position: absolute;
    left: 30px; top: 218px;
    width: 58px; height: 58px;
    border-radius: 50%;
    background: radial-gradient(circle at 40% 30%, var(--btn-light), var(--btn-dark) 75%);
    border: 2px solid #0d4f7a;
    box-sizing: border-box;
    display: flex;
    align-items: center;
    justify-content: center;
    text-align: center;
    font-family: "Arimo", sans-serif;
    font-weight: 700;
    font-size: 14px;
    line-height: 14px;
    color: #000;
    box-shadow: 0 5px 4px -2px rgba(0,0,0,0.5);
  }
  .cta-caption {
    position: absolute;
    left: 18px; bottom: 10px;
    margin: 0;
    font-family: "Anton", sans-serif;
    font-size: 14px;
    line-height: 16px;
    color: var(--ink-red);
  }
  .cta-caption .new {
    color: var(--ink-dark);
    font-size: 16px;
  }
  .brand {
    position: absolute;
    right: 18px; bottom: 12px;
    display: flex;
    align-items: center;
    gap: 4px;
    font-family: "Tinos", serif;
    font-size: 17px;
    color: var(--brand);
  }
  .brand-dot {
    width: 9px; height: 9px;
    border-radius: 50%;
    background: var(--brand);
  }
</style>
</head>
<body>

<section class="banner banner--alert">
  <div class="hero"><div class="hero-backdrop" role="img" aria-label="Faded rooftop of a house"></div></div>
  <div class="band"></div>
  <svg class="warning-sign" viewBox="0 0 116 102" aria-hidden="true">
    <polygon points="58,4 112,98 4,98" fill="var(--sign)" stroke="#222" stroke-width="6" stroke-linejoin="round"/>
    <polygon points="62,34 46,68 58,68 52,90 72,56 60,56 68,34" fill="#111"/>
  </svg>
  <h1 class="headline">Unexpected Drop<br>in Mortgage Rates</h1>
  <div class="cta-button">click<br>here</div>
  <p class="cta-caption">to calculate a<br><span class="new">NEW</span> payment</p>
  <div class="brand"><span class="brand-dot"></span>CopperLeafLoans</div>
</section>

<section class="banner banner--rate">
  <div class="hero"><div class="hero-backdrop" role="img" aria-label="Faded rooftop of a house"></div></div>
  <div class="band"></div>
  <p class="rate-lead">Refinance NOW at</p>
  <p class="rate-value">3.21%</p>
  <span class="rate-apr">APR*</span>
  <p class="fine-print">* Terms and Conditions apply</p>
  <div class="cta-button">click<br>here</div>
  <p class="cta-caption">to calculate a<br><span class="new">NEW</span> payment</p>
  <div class="brand"><span class="brand-dot"></span>CopperLeafLoans</div>
</section>

</body>
</html>
```